TEAL BEACON LICE REMOVAL labels

I need a label design for our MINT REPELLING SHAMPOO (LICE PREVENTION).
It also includes our MINT REPELLING CONDITIONER (LICE PREVENTION) and our MINT SPRAY (LICE PREVENTION) also includes LICE & NIT ELIMINATING MOUSSE (LICE TREATMENT) and a LICE ELIMINATOR 100% Dimethicone oil (LICE TREATMENT). The shampoo and conditioner are sulfate free, contains peppermint and other essential oils and is safe for the entire family. Label should be simple, modern and high end looking. Fun is good too if it looks nice!

Target Market(s)

Kids and Adults

Industry/Entity Type

Hair Care Product

Font styles to use
Sans Serif
Decorative

Requirements
Must have
• -Words that should be used: safe, non toxic, sulfate free, essential oils, pesticide free. - Naturally removes lice, super lice & nits are great words for the lice & nit eliminating mousse and treatment oil 100% Dimethicone oil
- On a side note there are no essential oils in the lice & nit eliminating mousse or treatment oil 100% Dimethicone oil
Nice to have
• Earth tone colors if possible
Kid safe, no fillers, colors or scents
100% effective (even against super lice)
8oz labels and 4oz labels
Should not have
• No pictures of lice

```html
<!DOCTYPE html>
<html lang="en">
<head>
<meta charset="utf-8">
<title>Teal Beacon Lice Removal – Mint Repelling Shampoo Label</title>
<link href="https://fonts.googleapis.com/css2?family=Quicksand:wght@300;400&family=Ubuntu:wght@300;500&family=Noto+Serif:ital,wght@1,400;1,700&display=swap" rel="stylesheet">
<style>
  :root {
    --ink: #1b1b1b;
    --accent: #e2582d;
    --paper: #ffffff;
    --frame: #6a2c8f;
    --grey: #3a3a3a;
  }
  * { margin: 0; padding: 0; box-sizing: border-box; }
  html, body { width: 1200px; height: 480px; overflow: hidden; background: var(--paper); }
  .canvas { position: relative; width: 1200px; height: 480px; }
  .label {
    position: absolute; left: 294px; top: 13px;
    width: 1056px; height: 780px;
    transform: scale(0.58); transform-origin: 0 0;
    border: 3px solid var(--frame); border-radius: 6px;
    background: var(--paper); color: var(--ink);
  }
  .label > * { position: absolute; }
  .serif { font-family: "Noto Serif", Georgia, serif; font-style: italic; }

  .brand-mark { display: flex; align-items: center; gap: 14px; }
  .brand-mark .dot { width: 44px; height: 44px; border-radius: 50%; background: var(--accent); flex: none; }
  .brand-mark .name {
    font-family: "Ubuntu", Arial, sans-serif; font-weight: 500; font-size: 22px;
    line-height: 1.15; letter-spacing: 2px; color: var(--ink);
  }
  .brand-mark.top { left: 32px; top: 100px; }
  .brand-mark.back { left: 800px; top: 535px; }
  .brand-mark.back .name { font-size: 18px; }

  .product-mint { left: 33px; top: 272px; font-family: "Ubuntu", Arial, sans-serif; font-weight: 300; font-size: 54px; line-height: 1; }
  .product-name { left: 31px; top: 326px; font-family: "Ubuntu", Arial, sans-serif; font-weight: 500; font-size: 68px; line-height: 1; }
  .product-type {
    left: -22px; top: 402px; width: 207px; height: 38px; background: var(--accent);
    color: var(--paper); font-family: "Quicksand", Arial, sans-serif; font-weight: 400;
    font-size: 34px; line-height: 36px; padding-left: 54px;
  }
  .claim { left: 33px; top: 448px; font-size: 23px; }
  .claim b { font-weight: 700; }

  .oil-badge { left: 248px; top: 518px; width: 78px; height: 78px; border-radius: 50%; border: 3px solid var(--ink); background: var(--accent); }

  .safety-band {
    left: 150px; top: 606px; width: 555px; height: 32px; background: var(--ink); color: var(--paper);
  }
  .safety-band .main { position: absolute; left: 28px; top: -2px; font-size: 26px; }
  .safety-band .sub { position: absolute; left: 268px; top: 6px; font-size: 17px; }

  .free-from { left: 40px; top: 642px; font-family: "Quicksand", Arial, sans-serif; font-weight: 400; font-size: 30px; }
  .efficacy { left: 418px; top: 642px; font-family: "Quicksand", Arial, sans-serif; font-size: 30px; }
  .efficacy small { display: block; font-size: 14px; margin-top: -4px; }
  .volume { left: 280px; top: 705px; font-size: 24px; }
  .volume b { font-size: 42px; font-weight: 400; }

  .tagline { left: 418px; top: 58px; font-size: 37px; line-height: 38px; }

  .info-column { left: 705px; top: 55px; width: 228px; }
  .info-column h3 { font-family: "Noto Serif", Georgia, serif; font-style: italic; font-weight: 400; font-size: 14px; margin-top: 4px; }
  .info-column p { font-family: "Quicksand", Arial, sans-serif; font-size: 11.4px; line-height: 14.1px; margin-bottom: 4px; }

  .upc-box { left: 952px; top: 32px; width: 70px; height: 168px; border: 3px solid var(--ink); }
  .upc-box span {
    position: absolute; left: 50%; top: 50%; transform: translate(-50%, -50%) rotate(-90deg);
    font-family: "Ubuntu", Arial, sans-serif; font-weight: 300; font-size: 46px;
  }
  .disposal-icons { left: 988px; top: 212px; }

  .contact-head { left: 718px; top: 440px; }
  .contact-head strong { display: block; font-size: 38px; font-weight: 700; line-height: 42px; }
  .contact-head span { display: block; font-size: 23px; line-height: 24px; }

  .brand-info {
    right: 32px; top: 652px; text-align: right;
    font-family: "Quicksand", Arial, sans-serif; font-size: 14px; line-height: 14.4px; color: var(--grey);
  }
</style>
</head>
<body>
<main class="canvas">
  <article class="label">
    <div class="brand-mark top">
      <span class="dot"></span>
      <span class="name">TEAL BEACON<br>LICE REMOVAL</span>
    </div>

    <h1 class="product-mint">Mint</h1>
    <h2 class="product-name">Repelling</h2>
    <div class="product-type">shampoo</div>
    <p class="claim serif"><b>lice prevention</b> for all family</p>

    <div class="oil-badge" aria-label="Essential oils badge"></div>

    <div class="safety-band serif">
      <span class="main">safe - non toxic</span>
      <span class="sub">Kid safe, no fillers, colors or scents</span>
    </div>
    <p class="free-from">sulfate &amp; pesticide free</p>
    <p class="efficacy">100% effective<small>(even against super lice)</small></p>
    <p class="volume serif"><b>8</b>fl oz</p>

    <p class="tagline serif">with our<br>natural &amp;<br>soft<br>formulation<br>removes lice,<br>super lice<br>&amp; nits</p>

    <section class="info-column">
      <h3>Directions</h3>
      <p>Lorem ipsum dolor sit amet, consectetuer adipiscing elit, sed diam nonummy nibh euismod tincidunt ut laoreet dolore magna aliquam erat volutpat. Ut wisi enim ad minim veniam, quis nostrud exerci tation ullamcorper suscipit lobortis nisl ut aliquip ex ea commodo consequat.</p>
      <h3>Caution</h3>
      <p>Lorem ipsum dolor sit amet, consectetuer adipiscing elit, sed diam nonummy nibh euismod tincidunt ut laoreet dolore magna aliquam erat volutpat. Ut wisi enim ad minim veniam, quis nostrud exerci tation ullamcorper suscipit lobortis nisl ut aliquip ex ea commodo consequat.</p>
      <h3>Ingredients</h3>
      <p>Lorem ipsum dolor sit amet, consectetuer adipiscing elit, sed diam nonummy nibh euismod tincidunt ut laoreet dolore magna aliquam erat volutpat. Ut wisi enim ad minim veniam, quis nostrud exerci tation ullamcorper suscipit lobortis nisl ut aliquip ex ea commodo consequat.</p>
    </section>

    <div class="upc-box"><span>UPC</span></div>

    <svg class="disposal-icons" width="36" height="110" viewBox="0 0 36 110" aria-label="Disposal and shelf-life marks">
      <rect x="4" y="2" width="26" height="26" fill="none" stroke="#1b1b1b" stroke-width="3"/>
      <path d="M4 44 L30 36" stroke="#1b1b1b" stroke-width="3"/>
      <rect x="4" y="48" width="28" height="18" rx="3" fill="none" stroke="#1b1b1b" stroke-width="2"/>
      <circle cx="20" cy="80" r="4" fill="#1b1b1b"/>
      <rect x="6" y="88" width="24" height="16" fill="#1b1b1b"/>
    </svg>

    <div class="contact-head serif">
      <strong>any question?</strong>
      <span>please contact us</span>
    </div>

    <div class="brand-mark back">
      <span class="dot"></span>
      <span class="name">TEAL BEACON<br>LICE REMOVAL</span>
    </div>

    <address class="brand-info" style="font-style:normal">
      Brand Information<br>office adreess<br>email adreess<br>web site<br>social media
    </address>
  </article>
</main>
</body>
</html>
```